corvapinecare needs a 4.6 handout

i need a styalized 4x6 postcard sized handout to leave on cars at shopping plazas and apartment buildings. WE are a medical marijuana referal clinic in brockton MA and we write perscriptions for qualifying patients, i have attached a pdf file of the content i need included in the hand out but please do not limit yourself if you feel like you could word it better. it is important to have our contact info front and center
Target Market(s)
potential medical marijuana patients
Industry/Entity Type
Apartment
Requirements
Must have
- the content listed inside the PDF file i attached
Nice to have
- must have everything in the PDF file. should be colorful and eye catching while still looking professional
Should not have
- pictures of cannabis buds or flowering plants.

```html
<!DOCTYPE html>
<html lang="en">
<head>
<meta charset="utf-8">
<title>corvapinecare – Medical Marijuana Card Handout</title>
<link href="https://fonts.googleapis.com/css2?family=Bebas+Neue&family=Lato:wght@300;400;700&display=swap" rel="stylesheet">
<style>
  :root {
    --page-bg: #d6d6d6;
    --card-bg: #ffffff;
    --brand-blue: #5b7cc0;
    --hours-blue: #5f80c2;
    --band-grey: #7f7f7f;
    --headline-grey: #6f6f6f;
    --text-white: #ffffff;
    --photo-light: #f3f5f8;
    --photo-mid: #dfe6ee;
  }
  * { box-sizing: border-box; margin: 0; padding: 0; }
  html, body {
    width: 1200px; height: 1200px; overflow: hidden;
    background: var(--page-bg);
    font-family: "Lato", Arial, sans-serif;
  }
  .handout {
    position: absolute; left: 40px; top: 280px;
    width: 1120px; height: 640px;
    background: var(--card-bg);
    overflow: hidden;
  }
  .headline { position: absolute; left: 62px; top: 34px; }
  .headline-lead {
    font-family: "Lato", Arial, sans-serif;
    font-weight: 300; font-size: 76px; line-height: 1;
    color: var(--headline-grey); letter-spacing: -1px;
  }
  .headline-main {
    font-family: "Bebas Neue", Impact, sans-serif;
    font-size: 96px; line-height: 0.9;
    color: var(--brand-blue); margin-top: 12px;
  }
  .team-photo {
    position: absolute; left: 610px; top: 60px;
    width: 510px; height: 440px;
    background: radial-gradient(ellipse at 60% 55%, var(--photo-mid) 0%, var(--photo-light) 55%, var(--card-bg) 85%);
  }
  .contact {
    position: absolute; left: 52px; top: 372px; width: 200px;
  }
  .brand-mark { display: flex; align-items: center; gap: 9px; }
  .brand-dot {
    width: 22px; height: 22px; border-radius: 50%; flex: none;
    background: var(--brand-blue);
  }
  .brand-name {
    font-family: "Lato", Arial, sans-serif;
    font-weight: 700; font-size: 24px; color: var(--brand-blue);
  }
  .contact-label {
    margin-top: 22px;
    font-family: "Lato", Arial, sans-serif; font-weight: 700;
    font-size: 16px; letter-spacing: 1px; text-transform: uppercase;
    color: var(--headline-grey);
  }
  .contact-phone {
    display: flex; align-items: center; gap: 8px; margin-top: 4px;
    font-family: "Lato", Arial, sans-serif; font-weight: 700;
    font-size: 26px; color: var(--brand-blue); white-space: nowrap;
  }
  .contact-city {
    margin-top: 6px;
    font-family: "Lato", Arial, sans-serif; font-weight: 400;
    font-size: 18px; color: var(--headline-grey);
  }
  .hours {
    position: absolute; left: 267px; top: 309px;
    width: 310px; height: 232px;
    background: var(--hours-blue); border-radius: 40px;
    padding: 30px 24px 0 22px;
    color: var(--text-white);
    font-family: "Lato", Arial, sans-serif; font-weight: 400;
    font-size: 27px; line-height: 34px;
    list-style: none;
  }
  .hours li { display: flex; align-items: baseline; }
  .hours .day { white-space: nowrap; }
  .hours .leader {
    flex: 1; border-bottom: 3px dotted var(--text-white);
    margin: 0 6px; transform: translateY(-6px);
  }
  .footer-shape { position: absolute; left: 0; top: 0; }
  .cta {
    position: absolute; left: 648px; top: 513px; width: 440px;
    color: var(--text-white);
    font-family: "Lato", Arial, sans-serif; font-weight: 400;
    font-size: 21px; line-height: 27px;
  }
  .cta strong { font-weight: 700; }
</style>
</head>
<body>
  <main class="handout">
    <div class="team-photo" role="img" aria-label="Photo of a smiling medical team in white coats giving thumbs up"></div>

    <h1 class="headline">
      <div class="headline-lead">Do you need a</div>
      <div class="headline-main">Medical Marijuana<br>Card?</div>
    </h1>

    <div class="contact">
      <div class="brand-mark">
        <span class="brand-dot"></span>
        <span class="brand-name">corvapinecare</span>
      </div>
      <div class="contact-label">Call today</div>
      <div class="contact-phone">
        <svg width="22" height="22" viewBox="0 0 24 24" aria-hidden="true"><path fill="var(--brand-blue)" d="M6.6 10.8a15.1 15.1 0 0 0 6.6 6.6l2.2-2.2c.3-.3.7-.4 1-.2 1.1.4 2.3.6 3.6.6.6 0 1 .4 1 1V20c0 .6-.4 1-1 1A17 17 0 0 1 3 4c0-.6.4-1 1-1h3.5c.6 0 1 .4 1 1 0 1.3.2 2.5.6 3.6.1.3 0 .7-.2 1L6.6 10.8z"/></svg>
        <span>(508) 555-0142</span>
      </div>
      <div class="contact-city">Brockton, MA</div>
    </div>

    <ul class="hours">
      <li><span class="day">Tuesday:</span><span class="leader"></span><span>9-5</span></li>
      <li><span class="day">Wednesday:</span><span class="leader"></span><span>9-5</span></li>
      <li><span class="day">Thursday:</span><span class="leader"></span><span>9-6</span></li>
      <li><span class="day">Friday:</span><span class="leader"></span><span>9-7</span></li>
      <li><span class="day">Saturday:</span><span class="leader"></span><span>9-3</span></li>
    </ul>

    <svg class="footer-shape" width="1120" height="640" viewBox="0 0 1120 640" aria-hidden="true">
      <path d="M0 590 H560 C585 590 596 578 600 555 L606 525 C610 502 624 490 650 490 H1120 V640 H0 Z" fill="var(--band-grey)"/>
    </svg>

    <p class="cta">There are over <strong>200</strong> qualifying conditions in the state of Massachusetts, call today to see if you qualify and book an appointment!</p>
  </main>
</body>
</html>
```